Carpentry company Needs a business card design

We need a design for a Carpentry / building company, business card. Please think of designs out of the ordinary and try to make it eye catching. Our existing logo will need to be incorporated in the design. However feel free to change the colours of the logo to suit your design. I would like to see some designs with green /black and orange incorporated into it.These are not the only colours accepted and all designs that appeal will be accepted.

Please contact me should you have any questions
Thanks Martin

Target Market(s)

General Public seeking carpentry work

Industry/Entity Type

Business

Contact Information for Business Card

- Current company logo ( colours can be changed)
-Phone number ,
- info@brelvanbuild.com.au
- brelvanbuild.com.au
-the facebook symbol

Font styles to use
Other font styles liked:
• You choose

Requirements
Must have
• Services we provide
• - Renovations
• -Deckings & Pergolas
• -Kitchens
• - Bathrooms
• - Intricate details
Nice to have
• an awesome design
Should not have
• Tools on the business card

```html
<!DOCTYPE html>
<html lang="en">
<head>
<meta charset="utf-8">
<title>Brelvan Build – Business Card</title>
<link rel="stylesheet" href="https://fonts.googleapis.com/css2?family=Michroma&display=swap">
<style>
  :root {
    --backdrop: #dcc39c;
    --black: #000000;
    --charcoal: #2b2a2a;
    --white: #ffffff;
    --green: #6cb33f;
    --orange: #f26f21;
    --ink: #231f20;
    --type: "Michroma", sans-serif;
  }
  * { margin: 0; padding: 0; box-sizing: border-box; }
  html, body { width: 1200px; height: 989px; overflow: hidden; }
  body { background: var(--backdrop); font-family: var(--type); position: relative; }

  .card { position: absolute; width: 425px; height: 717px; overflow: hidden; box-shadow: 0 10px 30px rgba(0,0,0,.35); }
  .card--front { left: 117px; top: 125px; }
  .card--back { left: 642px; top: 127px; }
  .card-shapes { position: absolute; inset: 0; }

  .site-url { position: absolute; top: 80px; width: 100%; text-align: center; color: var(--white); font-size: 15px; letter-spacing: 2px; }

  .brand { position: absolute; display: flex; align-items: center; gap: 12px; color: var(--ink); white-space: nowrap; }
  .brand-mark { width: 14px; height: 14px; background: var(--orange); flex: none; }
  .brand-name { line-height: 1.05; letter-spacing: 2px; }
  .card--front .brand { left: 52px; top: 262px; }
  .card--front .brand-name { font-size: 31px; }
  .card--back .brand { left: 92px; top: 104px; }
  .card--back .brand-name { font-size: 21px; }

  .services { position: absolute; left: 55px; top: 437px; }
  .services-title { color: var(--orange); font-size: 19px; letter-spacing: 3px; font-weight: normal; margin-bottom: 10px; }
  .services-list { list-style: none; margin-left: 23px; }
  .services-list li { color: var(--white); font-size: 16px; font-variant: small-caps; letter-spacing: 2.5px; line-height: 28.5px; position: relative; }
  .services-list li::before { content: ""; position: absolute; left: -19px; top: 10px; width: 8px; height: 8px; background: var(--orange); transform: rotate(45deg); }

  .person { position: absolute; left: 73px; top: 300px; color: var(--white); }
  .person-name { font-size: 19px; font-variant: small-caps; letter-spacing: 2.5px; font-weight: normal; }
  .person-role { font-size: 15px; font-variant: small-caps; letter-spacing: 2px; margin-top: 6px; }

  .contacts { position: absolute; left: 68px; top: 380px; list-style: none; color: var(--white); }
  .contacts li { display: flex; align-items: center; gap: 10px; height: 33.5px; letter-spacing: 1.5px; }
  .contacts .phone { font-size: 15px; }
  .contacts .web { font-size: 12.5px; }
  .contacts svg { width: 22px; height: 22px; flex: none; }

  .social-dot { position: absolute; left: 192px; top: 564px; width: 46px; height: 46px; border-radius: 50%; background: var(--orange); }
</style>
</head>
<body>

<section class="card card--front">
  <svg class="card-shapes" viewBox="0 0 425 717" aria-hidden="true">
    <rect width="425" height="717" fill="var(--white)"/>
    <polygon points="0,0 425,0 425,208 330,208 285,170 240,208 0,208" fill="var(--black)"/>
    <polyline points="0,210 240,210 285,172 330,210 425,210" fill="none" stroke="var(--green)" stroke-width="4"/>
    <rect x="0" y="382" width="425" height="335" fill="var(--charcoal)"/>
    <rect x="0" y="378" width="425" height="5" fill="var(--orange)"/>
  </svg>
  <p class="site-url">WWW.BRELVANBUILD.COM.AU</p>
  <div class="brand">
    <span class="brand-mark"></span>
    <span class="brand-name">BRELVAN<br>BUILD</span>
  </div>
  <div class="services">
    <h2 class="services-title">PROVIDED SERVICES:</h2>
    <ul class="services-list">
      <li>Renovations</li>
      <li>Deckings &amp; Pergolas</li>
      <li>Kitchens</li>
      <li>Bathrooms</li>
      <li>Intricate details</li>
    </ul>
  </div>
</section>

<section class="card card--back">
  <svg class="card-shapes" viewBox="0 0 425 717" aria-hidden="true">
    <rect width="425" height="717" fill="var(--black)"/>
    <polygon points="0,0 425,0 425,210 185,210 140,250 95,210 0,210" fill="var(--white)"/>
    <polyline points="0,211 95,211 140,251 185,211 425,211" fill="none" stroke="var(--green)" stroke-width="4"/>
  </svg>
  <div class="brand">
    <span class="brand-mark"></span>
    <span class="brand-name">BRELVAN<br>BUILD</span>
  </div>
  <div class="person">
    <h1 class="person-name">Your Name</h1>
    <p class="person-role">Position</p>
  </div>
  <ul class="contacts">
    <li class="phone">
      <svg viewBox="0 0 24 24" aria-hidden="true"><path d="M6 3l3 4-2 2c1 3 4 6 7 7l2-2 4 3-2 3C10 20 4 14 3 6z" fill="none" stroke="var(--orange)" stroke-width="2" stroke-linejoin="round"/></svg>
      123-456-7890
    </li>
    <li class="phone">
      <svg viewBox="0 0 24 24" aria-hidden="true"><rect x="7" y="3" width="10" height="18" rx="2" fill="none" stroke="var(--orange)" stroke-width="2"/><line x1="11" y1="18" x2="13" y2="18" stroke="var(--orange)" stroke-width="2"/></svg>
      123-456-7888
    </li>
    <li class="web">
      <svg viewBox="0 0 24 24" aria-hidden="true"><rect x="3" y="6" width="18" height="12" fill="none" stroke="var(--orange)" stroke-width="2"/><polyline points="3,6 12,13 21,6" fill="none" stroke="var(--orange)" stroke-width="2"/></svg>
      info@brelvanbuild.com.au
    </li>
    <li class="web">
      <svg viewBox="0 0 24 24" aria-hidden="true"><circle cx="12" cy="12" r="9" fill="none" stroke="var(--orange)" stroke-width="2"/><ellipse cx="12" cy="12" rx="4" ry="9" fill="none" stroke="var(--orange)" stroke-width="1.5"/><line x1="3" y1="12" x2="21" y2="12" stroke="var(--orange)" stroke-width="1.5"/></svg>
      www.brelvanbuild.com.au
    </li>
  </ul>
  <span class="social-dot" role="img" aria-label="Social media link"></span>
</section>

</body>
</html>
```